A register your interest postcard

It is a slightly bigger postcard that wil be inserted inside a brochure. On one side it is to have the logo with the statement "at Corvanne, Byron Bay" underneath. At the bottom it is to say "Register your interest to become an owner at The Keyholders Circle. On the flipside it has the logo in a smaller version with again in smaller writing "Become an owner at The Keyholders Circle". The main point of this side it to say " SMS your name to 0491 562 037 OR Name: Email: Phone:".
I would like a wood-look style postcard. It is for a luxury beach property that uses a lot of distressed wood in the building of the houses.
Industry/Entity Type
Building
Contact Information for Business Card
I would like a wood-look style postcard for a beach property.
Look and feel
Each slider illustrates characteristics of the customer's brand and the style your logo design should communicate.

```html
<!DOCTYPE html>
<html lang="en">
<head>
<meta charset="utf-8">
<title>The Keyholders Circle – Register your interest</title>
<link href="https://fonts.googleapis.com/css2?family=Roboto+Condensed:wght@400;700&display=swap" rel="stylesheet">
<style>
  :root {
    --white: #ffffff;
    --ink: #1b1b1b;
    --red: #e0201c;
    --slate: #435052;
    --water-top: #5d6668;
    --water-mid: #2c3638;
    --water-deep: #151b1c;
    --deck: #6f6a63;
  }
  html, body {
    margin: 0;
    padding: 0;
    width: 1200px;
    height: 855px;
    overflow: hidden;
    background: var(--white);
  }
  .postcard {
    position: relative;
    width: 1200px;
    height: 855px;
    overflow: hidden;
    font-family: "Roboto Condensed", "Arial Narrow", sans-serif;
    color: var(--white);
  }
  .scene {
    position: absolute;
    inset: 0;
    background:
      linear-gradient(115deg, transparent 48%, rgba(120,114,106,0.55) 62%, rgba(90,86,80,0.7) 100%),
      linear-gradient(180deg, var(--water-top) 0%, #4a5456 22%, var(--water-mid) 55%, var(--water-deep) 100%);
  }
  .brand-panel {
    position: absolute;
    left: 0;
    top: 0;
    width: 500px;
    height: 330px;
    background: var(--white);
  }
  .brand-name {
    position: absolute;
    left: 34px;
    top: 22px;
    margin: 0;
    font-weight: 700;
    font-size: 82px;
    line-height: 92px;
    letter-spacing: 2px;
    text-transform: uppercase;
    color: var(--ink);
  }
  .location-band {
    position: absolute;
    left: 0;
    top: 330px;
    width: 500px;
    height: 58px;
    background: var(--red);
    border-top: 3px solid var(--white);
    box-sizing: border-box;
    font-weight: 700;
    font-size: 32px;
    line-height: 55px;
    padding-left: 48px;
  }
  .headline {
    position: absolute;
    left: 662px;
    top: 112px;
    margin: 0;
    width: 520px;
    font-weight: 700;
    font-size: 80px;
    line-height: 94px;
  }
  .headline span {
    background: var(--slate);
    padding: 0 10px;
    border-radius: 10px;
    box-decoration-break: clone;
    -webkit-box-decoration-break: clone;
  }
  .invite {
    position: absolute;
    left: 677px;
    top: 512px;
    margin: 0;
    font-weight: 400;
    font-size: 41px;
    line-height: 54px;
  }
  .contact-bar {
    position: absolute;
    left: 0;
    top: 777px;
    width: 1118px;
    height: 58px;
    background: var(--red);
    font-size: 35px;
    line-height: 58px;
    padding-left: 84px;
    box-sizing: border-box;
    white-space: nowrap;
  }
  .base-strip {
    position: absolute;
    left: 0;
    top: 835px;
    width: 1200px;
    height: 20px;
    background: var(--water-deep);
  }
  .monogram {
    position: absolute;
    left: 1124px;
    top: 692px;
    width: 62px;
    height: 146px;
    background: var(--white);
    color: var(--ink);
    font-weight: 700;
    font-size: 40px;
    line-height: 50px;
    text-align: center;
    padding-top: 22px;
    box-sizing: border-box;
  }
</style>
</head>
<body>
  <main class="postcard">
    <div class="scene" role="img" aria-label="Photograph of a weathered timber jetty stretching over calm dark water towards a headland"></div>

    <div class="brand-panel">
      <h1 class="brand-name">The<br>Keyholders<br>Circle</h1>
    </div>
    <div class="location-band">"at Corvanne, Byron Bay"</div>

    <h2 class="headline"><span>Become<br>an owner at<br>The Keyholders<br>Circle</span></h2>

    <p class="invite">Register your interest<br>to become an owner<br>at The Keyholders Circle</p>

    <div class="contact-bar">SMS your name to 0491 562 037 OR Name: Email: Phone:</div>
    <div class="base-strip"></div>

    <div class="monogram">K<br>C</div>
  </main>
</body>
</html>
```